I sell carved wood signs on line and need business cards for every order that gets mailed out
Business name- Brindlefox
Website address/ email address/ name /

```html
<!DOCTYPE html>
<html lang="en">
<head>
<meta charset="utf-8">
<title>Brindlefox Business Card</title>
<link rel="stylesheet" href="https://fonts.googleapis.com/css2?family=Montserrat:wght@700;800&family=Open+Sans:wght@400;600&display=swap">
<style>
  :root {
    --backdrop: #2b2b2d;
    --card-black: #0a0a0a;
    --brand-green: #3ec454;
    --stripe-grey: #4a4a4c;
    --divider-grey: #6a6a6a;
    --text-white: #f2f2f2;
    --text-soft: #d6d6d6;
  }
  * { box-sizing: border-box; margin: 0; padding: 0; }
  html, body {
    width: 1200px;
    height: 960px;
    overflow: hidden;
    background: var(--backdrop);
  }
  .canvas {
    position: relative;
    width: 1200px;
    height: 960px;
  }
  .card {
    position: absolute;
    width: 640px;
    height: 366px;
    background: var(--card-black);
    border-radius: 22px;
    overflow: hidden;
    box-shadow: 0 18px 40px rgba(0, 0, 0, 0.45);
  }
  .card--front { left: 120px; top: 90px; }
  .card--back { left: 440px; top: 500px; }

  /* Front */
  .front-brand {
    position: absolute;
    inset: 0;
    display: flex;
    align-items: center;
    justify-content: center;
    gap: 18px;
  }
  .brand-dot {
    width: 34px;
    height: 34px;
    border-radius: 50%;
    background: var(--brand-green);
  }
  .brand-name {
    font-family: "Montserrat", sans-serif;
    font-weight: 800;
    font-size: 54px;
    letter-spacing: 1px;
    text-transform: uppercase;
    color: var(--brand-green);
  }

  /* Back */
  .back-wave {
    position: absolute;
    left: 0;
    bottom: 0;
    width: 640px;
    height: 366px;
  }
  .back-brand {
    position: absolute;
    left: 40px;
    top: 118px;
    width: 250px;
    display: flex;
    flex-direction: column;
    align-items: center;
    gap: 14px;
  }
  .back-brand .brand-dot { width: 40px; height: 40px; }
  .back-brand .brand-name { font-size: 34px; }
  .divider {
    position: absolute;
    left: 318px;
    top: 70px;
    width: 2px;
    height: 178px;
    background: var(--divider-grey);
  }
  .details {
    position: absolute;
    left: 340px;
    top: 52px;
    width: 280px;
    font-family: "Open Sans", sans-serif;
    color: var(--text-white);
  }
  .person-name {
    font-family: "Montserrat", sans-serif;
    font-weight: 800;
    font-size: 24px;
    color: var(--brand-green);
    text-transform: uppercase;
    letter-spacing: 0.5px;
  }
  .name-rule {
    width: 180px;
    height: 3px;
    background: var(--brand-green);
    margin: 4px 0 6px;
  }
  .person-title {
    font-size: 16px;
    font-weight: 600;
    margin-bottom: 16px;
  }
  .address {
    font-size: 14px;
    line-height: 1.35;
    color: var(--text-soft);
    margin-bottom: 14px;
  }
  .contact-list { list-style: none; }
  .contact-item {
    display: flex;
    align-items: center;
    gap: 10px;
    font-size: 15px;
    line-height: 1.5;
  }
  .contact-icon { width: 14px; height: 14px; flex: none; }
</style>
</head>
<body>
<main class="canvas">

  <section class="card card--front" aria-label="Card front">
    <div class="front-brand">
      <span class="brand-dot"></span>
      <span class="brand-name">Brindlefox</span>
    </div>
  </section>

  <section class="card card--back" aria-label="Card back">
    <svg class="back-wave" viewBox="0 0 640 366" aria-hidden="true">
      <path d="M0,300 C150,282 250,348 400,326 C500,310 580,250 640,214 L640,366 L0,366 Z" fill="var(--stripe-grey)"/>
      <path d="M0,307 C150,289 250,355 400,333 C500,317 580,257 640,222 L640,366 L0,366 Z" fill="var(--card-black)"/>
      <path d="M0,318 C150,300 250,366 400,344 C500,328 580,268 640,234 L640,366 L0,366 Z" fill="var(--brand-green)"/>
    </svg>

    <div class="back-brand">
      <span class="brand-dot"></span>
      <span class="brand-name">Brindlefox</span>
    </div>

    <div class="divider"></div>

    <div class="details">
      <h1 class="person-name">Elena Marsh</h1>
      <div class="name-rule"></div>
      <p class="person-title">Director</p>
      <p class="address">Unit 4, 18 Harbour Lane<br>Portview NSW 2031</p>
      <ul class="contact-list">
        <li class="contact-item">
          <svg class="contact-icon" viewBox="0 0 24 24" aria-hidden="true"><path fill="var(--brand-green)" d="M6.6 10.8a15 15 0 0 0 6.6 6.6l2.2-2.2a1 1 0 0 1 1-.25 11.4 11.4 0 0 0 3.6.57 1 1 0 0 1 1 1V20a1 1 0 0 1-1 1A17 17 0 0 1 3 4a1 1 0 0 1 1-1h3.5a1 1 0 0 1 1 1c0 1.25.2 2.45.57 3.57a1 1 0 0 1-.25 1z"/></svg>
          <span>(555) 318-4206</span>
        </li>
        <li class="contact-item">
          <svg class="contact-icon" viewBox="0 0 24 24" aria-hidden="true"><rect x="2" y="5" width="20" height="14" rx="1.5" fill="var(--brand-green)"/><path d="M3 6l9 7 9-7" fill="none" stroke="var(--card-black)" stroke-width="2"/></svg>
          <span>hello@brindlefox.com</span>
        </li>
        <li class="contact-item">
          <svg class="contact-icon" viewBox="0 0 24 24" aria-hidden="true"><circle cx="12" cy="12" r="10" fill="var(--brand-green)"/><path d="M2 12h20M12 2c3 3 3 17 0 20M12 2c-3 3-3 17 0 20" fill="none" stroke="var(--card-black)" stroke-width="1.6"/></svg>
          <span>www.brindlefox.com</span>
        </li>
      </ul>
    </div>
  </section>

</main>
</body>
</html>
```